Aviation Consultant Seeking a Business Wordpress Site

I am looking for a Wordpress website for my small (it's just me) airport noise consulting firm. We work with airports to address aircraft noise issues in nearby communities. We also work with communities to help them understand aircraft noise and flight operations, air traffic control, etc., and to come up with strategies for collaborating with the airport to address noise and overflight issues.

I'd like a contemporary design that is both professional and modern.

My firm's services include establishing noise abatement programs for airports, working with airports, aviation industry (airlines, air traffic controllers, airports), and the community (neighborhoods located near noisy airports), to reduce noise impacts associated with aircraft operations.

My clients are primarily airports, but I also work with communities located near airports.

We provide technical support to help communities understand the complexities of aircraft noise and aviation. We also work to help airports understand the interests and concerns of their community.

Our tagline is: "Advocate | Collaborate | Engage"

and "bridging the gap between airports and their communities"

A couple examples of site designs I love are:

http://slidecraftstudio.example.co.uk/
http://www.quirkfox.example.com/
http://sunrisetendwell.example.com/

I found this template which I like a lot: http://glidepanelsampler.example.com/ I'm wondering if they have similar templates for Wordpress.

I am very open to your recommendations on design. I've worked on two projects on PixelHarbor and have been extremely pleased with the outcomes.

Thank you for your interest in my project!

Target Market(s)

Airports, communities located near airports, city governments, national airway directorate

Industry/Entity Type

Airport

Font styles to use
Sans Serif

Requirements
Must have
• Professional look and feel.
Nice to have
• I envision a one page website (with multiple sections that you can scroll up/down to like the template I listed above. I am open to multiple pages if you think that would look/work better. Sections would include:
• Welcome (top section or home page)
• Who We Are
• What We Do
• Why RNV?
• Contact Us
• Within the What We Do section, there will be graphics representing specialty areas such as:
• Noise Office Management
• Noise Program Development/Expansion
• Fly Quiet Programs
• Stakeholder Engagement
• SkyPath / PBN
• These are just ideas. I am open to your expert recommendations and creativity.
• Here are some wordpress templates I like:
• http://demo.layoutmint.example.com/?theme=solo&device=desktop&_ga=1.480215637.9083716254.2749183065
• http://skinworks.example/demo/themes/layered/#
• http://layoutbazaar.example.net/item/q-the-skin/full_screen_preview/3160482
• http://lumora.skins.example
Should not have
• Should not be a blog or designed like a blog. I do not plan on a blogging component. This should be designed as a modern, small business website.

```html
<!DOCTYPE html>
<html lang="en">
<head>
<meta charset="utf-8">
<title>Runway Noise Ventures</title>
<link rel="stylesheet" href="https://fonts.googleapis.com/css2?family=Cinzel:wght@400;600;700&family=Arimo:wght@400;700&display=swap">
<style>
:root{
  --ink:#1b1b1b;
  --text:#333333;
  --brand:#2f5ea8;
  --brand-dark:#1f4f96;
  --blue-light:#3f72b8;
  --submit:#4a72b0;
  --pale:#e0ebfb;
  --pale-hover:#c9daf3;
  --field:#f2f2f2;
  --field-line:#c9c9c9;
  --required:#d9534f;
  --footer:#666666;
  --white:#ffffff;
  --sky-top:#5f93c9;
  --sky-mid:#a9c6e2;
  --cloud:#e6edf4;
}
*{box-sizing:border-box;margin:0;padding:0}
html,body{width:1200px;height:2691px;overflow:hidden}
body{position:relative;background:var(--white);font-family:"Arimo",Arial,sans-serif;color:var(--text)}
.heading{font-family:"Cinzel",Georgia,serif;font-weight:400;color:var(--ink);text-align:center;letter-spacing:1px}

/* header */
.site-header{position:absolute;left:0;top:0;width:1200px;height:102px;background:var(--white)}
.brand{position:absolute;left:100px;top:12px;display:flex;align-items:center;gap:12px;height:78px}
.brand-dot{width:78px;height:78px;border-radius:50%;background:var(--brand)}
.brand-name{font-family:"Arimo",Arial,sans-serif;font-size:24px;color:var(--brand);text-transform:uppercase;letter-spacing:.5px}
.main-nav{position:absolute;right:98px;top:39px;display:flex;font-size:14.5px;color:#444}
.main-nav a{color:inherit;text-decoration:none;padding:0 12px;border-left:1px solid #bbb;line-height:24px}
.main-nav a:first-child{border-left:none}

/* hero */
.hero{position:absolute;left:0;top:102px;width:1200px;height:603px;overflow:hidden}
.hero-photo{position:absolute;inset:0;background:linear-gradient(180deg,var(--sky-top) 0%,var(--sky-mid) 45%,var(--cloud) 75%,#c3d2e0 100%)}
.hero-title{position:absolute;left:104px;top:198px;font-family:"Cinzel",Georgia,serif;font-weight:700;font-size:76px;color:#111;letter-spacing:1px;line-height:1}
.hero-sub{position:absolute;left:106px;top:284px;font-family:"Cinzel",Georgia,serif;font-weight:600;font-size:26px;color:#111;letter-spacing:2px}
.hero-arrow{position:absolute;top:226px}
.hero-arrow.prev{left:30px}
.hero-arrow.next{right:30px}

/* welcome */
.welcome{position:absolute;left:0;top:705px;width:1200px;height:384px}
.welcome .heading{position:absolute;top:49px;width:100%;font-size:33px;font-weight:600;letter-spacing:1.5px}
.welcome-copy{position:absolute;left:150px;top:110px;width:900px;text-align:center;font-size:14px;line-height:22px;color:#333}
.welcome-copy p+p{margin-top:18px}
.read-more{position:absolute;left:484px;top:277px;width:189px;height:52px;border:2px solid #111;font-family:"Cinzel",Georgia,serif;font-weight:700;font-size:18px;color:#111;display:flex;align-items:center;justify-content:center;letter-spacing:1px}

/* who we are */
.who{position:absolute;left:0;top:1089px;width:1200px;height:409px;background:linear-gradient(135deg,var(--brand-dark) 0%,#2a5da5 50%,var(--blue-light) 100%);overflow:hidden}
.who-facet{position:absolute;inset:0}
.who .heading{position:absolute;top:50px;width:100%;font-size:46px;font-weight:600;color:var(--white)}
.who-copy{position:absolute;left:112px;top:140px;width:976px;text-align:center;font-size:18px;line-height:26px;color:var(--white)}
.who-copy p+p{margin-top:26px}

/* what we do */
.services{position:absolute;left:0;top:1498px;width:1200px;height:499px;background:var(--pale)}
.services .heading{position:absolute;top:66px;width:100%;font-size:46px;font-weight:600}
.service{position:absolute;top:167px;width:232px;height:271px;text-align:center}
.service.is-active{background:var(--pale-hover)}
.service-badge{width:122px;height:122px;margin:18px auto 0;border-radius:50%;background:var(--white);border:3px solid #c6d5ee;display:flex;align-items:center;justify-content:center}
.service-badge span{width:92px;height:92px;border-radius:50%;background:var(--brand)}
.service p{margin:30px auto 0;width:190px;font-size:15px;line-height:22px;color:#222}

/* contact */
.contact{position:absolute;left:0;top:1997px;width:1200px;height:638px}
.contact .heading{position:absolute;top:53px;width:100%;font-size:46px;font-weight:600}
.field{position:absolute;background:var(--field);border:1px solid var(--field-line);border-radius:3px;font-size:14px;color:#888;padding:18px 10px 0}
.field em{color:var(--required);font-style:normal}
.submit{position:absolute;left:755px;top:540px;width:135px;height:45px;background:var(--submit);border-radius:4px;color:var(--white);font-family:"Cinzel",Georgia,serif;font-weight:600;font-size:22px;display:flex;align-items:center;justify-content:center;letter-spacing:1px}

/* footer */
.site-footer{position:absolute;left:0;top:2635px;width:1200px;height:56px;background:var(--footer);color:var(--white);font-size:13px}
.copyright{position:absolute;left:104px;top:20px}
.footer-links{position:absolute;right:100px;top:16px;display:flex;gap:22px;align-items:center}
.footer-dot{width:24px;height:24px;border-radius:50%;background:var(--white)}
</style>
</head>
<body>

<header class="site-header">
  <div class="brand">
    <span class="brand-dot"></span>
    <span class="brand-name">Runway Noise Ventures</span>
  </div>
  <nav class="main-nav">
    <a href="#welcome">Welcome</a>
    <a href="#who">Who We Are</a>
    <a href="#what">What We do</a>
    <a href="#why">Why RNV?</a>
    <a href="#contact">Contact</a>
  </nav>
</header>

<section class="hero">
  <div class="hero-photo" role="img" aria-label="Photo of a passenger jet flying head-on above a sea of white clouds under a blue sky"></div>
  <h1 class="hero-title">AIRCRAFT</h1>
  <p class="hero-sub">ENGINEERS LOOK THAT</p>
  <svg class="hero-arrow prev" width="26" height="40" viewBox="0 0 26 40"><polyline points="22,3 5,20 22,37" fill="none" stroke="#111" stroke-width="3"/></svg>
  <svg class="hero-arrow next" width="26" height="40" viewBox="0 0 26 40"><polyline points="4,3 21,20 4,37" fill="none" stroke="#111" stroke-width="3"/></svg>
</section>

<section class="welcome" id="welcome">
  <h2 class="heading">WELCOME TO RUNWAY NOISE VENTURES</h2>
  <div class="welcome-copy">
    <p>Lorem Ipsum is simply dummy text of the printing and typesetting industry. Lorem Ipsum has been the industry's standard dummy text ever since the 1500s, when an unknown printer took a galley of type and scrambled it to make a type specimen book. It has survived not only five centuries, but also the leap into electronic typesetting, remaining essentially unchanged.</p>
    <p>It was popularised in the 1960s with the release of Typeleaf sheets containing Lorem Ipsum passages, and more recently with desktop publishing software like Quillset Composer including versions of Lorem Ipsum.</p>
  </div>
  <a class="read-more">READ MORE</a>
</section>

<section class="who" id="who">
  <svg class="who-facet" width="1200" height="409" viewBox="0 0 1200 409">
    <polygon points="300,0 700,0 520,409 200,409" fill="#ffffff" opacity="0.04"/>
    <polygon points="760,0 1200,0 1200,260" fill="#ffffff" opacity="0.05"/>
    <polygon points="0,120 260,409 0,409" fill="#000000" opacity="0.05"/>
  </svg>
  <h2 class="heading">WHO WE ARE</h2>
  <div class="who-copy">
    <p>Lorem Ipsum is simply dummy text of the printing and typesetting industry. Lorem Ipsum has been the industry's standard dummy text ever since the 1500s, when an unknown printer took a galley of type and scrambled it to make a type specimen book. It has survived not only five centuries, but also the leap into electronic typesetting, remaining essentially unchanged.</p>
    <p>It was popularised in the 1960s with the release of Typeleaf sheets containing Lorem Ipsum passages, and more recently with desktop publishing software like Quillset Composer including versions of Lorem Ipsum.</p>
  </div>
</section>

<section class="services" id="what">
  <h2 class="heading">WHAT WE DO</h2>
  <div class="service" style="left:85px"><div class="service-badge"><span></span></div><p>Lorem Ipsum has been the industry's standard dummy text ever 1500s</p></div>
  <div class="service is-active" style="left:348px"><div class="service-badge"><span></span></div><p>Lorem Ipsum has been the industry's standard dummy text ever 1500s</p></div>
  <div class="service" style="left:612px"><div class="service-badge"><span></span></div><p>Lorem Ipsum has been the industry's standard dummy text ever 1500s</p></div>
  <div class="service" style="left:876px"><div class="service-badge"><span></span></div><p>Lorem Ipsum has been the industry's standard dummy text ever 1500s</p></div>
</section>

<section class="contact" id="contact">
  <h2 class="heading">CONTACT US</h2>
  <div class="field" style="left:240px;top:154px;width:305px;height:54px">First Name<em>*</em></div>
  <div class="field" style="left:594px;top:154px;width:298px;height:54px">Last Name<em>*</em></div>
  <div class="field" style="left:240px;top:240px;width:305px;height:54px">Phone<em>*</em></div>
  <div class="field" style="left:594px;top:240px;width:298px;height:54px">Email<em>*</em></div>
  <div class="field" style="left:239px;top:321px;width:653px;height:54px">Airport/Organization<em>*</em></div>
  <div class="field" style="left:239px;top:398px;width:653px;height:113px">Message<em>*</em></div>
  <a class="submit">SUBMIT</a>
</section>

<footer class="site-footer">
  <p class="copyright">© 2015 Runway Noise Ventures. All Rights Reserved.</p>
  <div class="footer-links">
    <span class="footer-dot"></span>
    <span class="footer-dot"></span>
    <svg width="28" height="20" viewBox="0 0 28 20"><rect x="1" y="1" width="26" height="18" fill="#fff"/><polyline points="1,1 14,11 27,1" fill="none" stroke="#666" stroke-width="2"/></svg>
  </div>
</footer>

</body>
</html>
```